Web Design Project

Our Field and scope of work is mainly on Oil and Gas tools and equipment rentals.
our main objective is to have a web design that can represent our rentals offering , both products and services.
go through the main design and draw the design out line , then we will add the contents.
Updates

company profile uploaded

Target Market(s)

Engineers and operations manager , for Oil and Gas.

Font styles to use
Sans Serif

Colors
00a990
87d0c7
33a6d7
3277b5
0355a3
cadf82

Requirements
Must have
• The Web must have the option to upgrade easily.
the contents should reflect Modern , eco friendly.
Nice to have
• - Green and Blue colors.
- Same fonts all contents.

```html
<!DOCTYPE html>
<html lang="en">
<head>
<meta charset="utf-8">
<title>Rigline – Rental Equipment and Tools</title>
<link rel="stylesheet" href="https://fonts.googleapis.com/css2?family=Roboto:wght@300;400;700&family=Arimo:wght@400;700&display=swap">
<style>
:root{
  --bg-blue:#1f5fa9;
  --bg-deep:#144d92;
  --brand-blue:#0355a3;
  --mid-blue:#3277b5;
  --sky:#33a6d7;
  --teal:#00a990;
  --mint:#87d0c7;
  --lime:#cadf82;
  --text:#7a7a7a;
  --rule:#d8d8d8;
  --footer-rule:#8fb3dc;
  --white:#ffffff;
}
*{box-sizing:border-box;margin:0;padding:0}
html,body{width:1127px;height:1200px;overflow:hidden}
body{
  position:relative;
  font-family:"Arimo",Arial,sans-serif;
  background:radial-gradient(ellipse at 50% 40%,#2a6cb6 0%,var(--bg-blue) 45%,var(--bg-deep) 100%);
  color:var(--white);
}
.abs{position:absolute}

/* top bar */
.follow-note{left:120px;top:8px;width:237px;text-align:right;font-size:8.5px;line-height:11px;color:#b9d1ec}
.top-divider{left:367px;top:8px;width:1px;height:23px;background:#5b8ac3}
.social{top:12px;width:12px;height:12px;border-radius:2px}
.phone-line{left:518px;top:6px;display:flex;align-items:center;gap:5px;font-size:12px;color:#d7e5f5}
.search-label{left:743px;top:13px;font-size:9px;color:#d7e5f5}
.search-input{left:803px;top:7px;width:138px;height:23px;background:var(--white);font-size:8px;color:#c4c4c4;padding:7px 6px}
.search-btn{left:941px;top:7px;width:23px;height:23px;background:var(--teal);display:flex;align-items:center;justify-content:center}

/* page panel */
.panel{left:159px;top:43px;width:806px;height:923px;background:var(--white);box-shadow:0 0 12px rgba(0,0,0,.3)}

.brand{left:185px;top:62px;display:flex;align-items:center;gap:7px}
.brand-mark{width:16px;height:16px;background:var(--sky)}
.brand-name{font-family:"Roboto",sans-serif;font-weight:700;font-size:28px;color:var(--brand-blue);letter-spacing:1px}
.brand-tag{left:213px;top:110px;font-size:7px;color:#555;letter-spacing:.4px}

.nav{left:559px;top:73px;display:flex;align-items:center;font-size:9.5px;color:#666}
.nav a{color:#666;text-decoration:none;margin-right:19px}
.nav .active{background:var(--brand-blue);color:var(--white);padding:7px 11px;border-radius:2px;margin-right:8px}
.nav-rule{left:389px;top:118px;width:553px;height:1px;background:var(--rule)}

.hero{left:185px;top:131px;width:759px;height:321px;
  background:linear-gradient(180deg,#7fb3df 0%,#3f85c7 35%,#1c5d9c 60%,#143f6f 100%);
  box-shadow:0 8px 8px -4px rgba(0,0,0,.35)}
.hero-title{left:493px;top:262px;font-family:"Roboto",sans-serif;font-weight:700;font-size:24px;color:var(--white);letter-spacing:-.5px}
.hero-copy{left:493px;top:291px;width:310px;font-size:10px;line-height:14.5px;color:var(--white);text-transform:uppercase;letter-spacing:-.2px}
.hero-btn{top:339px;height:21px;width:60px;font-size:11px;display:flex;align-items:center;justify-content:center;gap:5px}
.hero-btn.login{left:493px;background:var(--lime);color:#1d3b1d}
.hero-btn.join{left:559px;background:var(--teal);color:var(--white)}

.dots{left:885px;top:472px;display:flex;gap:3px}
.dots span{width:9px;height:9px;border-radius:50%;background:#c4c4c4;box-shadow:inset 0 1px 2px rgba(0,0,0,.3)}
.dots .on{background:#555}

.h-section{font-family:"Roboto",sans-serif;font-weight:300;font-size:16px;color:var(--brand-blue);white-space:nowrap}
.h-section em{font-style:normal;color:var(--teal)}
.h-rule{height:1px;background:var(--rule)}

.intro{left:185px;top:510px;width:755px;font-size:8.4px;line-height:16px;color:var(--text)}
.more{height:20px;width:66px;border:1px solid #cfcfcf;border-radius:2px;background:linear-gradient(#fff,#eee);color:#555;font-size:8px;display:flex;align-items:center;justify-content:center;gap:9px;box-shadow:0 1px 2px rgba(0,0,0,.15)}
.more::after{content:"";width:0;height:0;border-left:5px solid #aaa;border-top:4px solid transparent;border-bottom:4px solid transparent}

.col-img{top:675px;width:180px;height:128px}
.col-list{top:819px;list-style:none;font-size:8.4px;line-height:14.5px;color:var(--text)}
.col-list li{position:relative;padding-left:13px;white-space:nowrap}
.col-list li::before{content:"";position:absolute;left:2px;top:4px;width:6px;height:6px;border-radius:50%;background:#333;box-shadow:inset 0 0 0 1.5px #333,inset 0 0 0 3px #fff}

/* footer */
.f-head{top:975px;font-family:"Roboto",sans-serif;font-weight:300;font-size:14.5px;color:var(--white)}
.f-list{list-style:none;font-size:8.5px;color:var(--white)}
.f-list li{height:24.15px;line-height:24px;padding-left:12px;border-bottom:1px solid var(--footer-rule);position:relative;white-space:nowrap;overflow:visible}
.f-list li:last-child{border-bottom:none}
.f-list li::before{content:"";position:absolute;left:2px;top:9px;border-left:4px solid #fff;border-top:3px solid transparent;border-bottom:3px solid transparent}
.quote{left:363px;top:1004px;width:180px;font-size:8.5px;line-height:16.1px}
.quote-rule{left:363px;top:1109px;width:181px;height:1px;background:var(--footer-rule)}
.quote-by{left:363px;top:1118px;font-size:8.5px;white-space:nowrap}
.contact{left:795px;top:998px;font-size:8.5px;line-height:16.1px;white-space:nowrap}
.top-btn{left:891px;top:970px;width:31px;height:31px;border-radius:50%;background:#3fd6c2;border:2px solid #b4efe7;font-size:8px;font-weight:700;color:var(--white);display:flex;flex-direction:column;align-items:center;justify-content:center;line-height:8px}
.top-line{left:906px;top:947px;width:1px;height:68px;background:#7aa3d3}
.foot-rule{left:161px;top:1154px;width:805px;height:1px;background:var(--footer-rule)}
.copyright{left:161px;top:1169px;font-size:9.5px}
.subscribe{left:492px;top:1167px;font-size:9px;font-weight:700;line-height:11px}
.sub-input{left:563px;top:1167px;width:99px;height:20px;background:#e9e9e9;color:#9a9a9a;font-size:8px;padding:6px 7px}
.sub-btn{left:662px;top:1167px;width:54px;height:20px;background:var(--teal);font-size:10px;font-weight:700;display:flex;align-items:center;justify-content:center}
</style>
</head>
<body>

<p class="abs follow-note">Follow us on the social network sites for the latest updates on our projects or so.</p>
<div class="abs top-divider"></div>
<span class="abs social" style="left:379px;background:#f08a24"></span>
<span class="abs social" style="left:395px;background:#3b5b9a"></span>
<span class="abs social" style="left:411px;background:#e6e6e6"></span>
<span class="abs social" style="left:427px;background:#4fb8e8"></span>
<div class="abs phone-line">
  <svg width="25" height="25" viewBox="0 0 25 25"><circle cx="12.5" cy="12.5" r="11" fill="none" stroke="#d7e5f5" stroke-width="1.5"/><path d="M9 7c1 0 2 2.5 1.5 3.2l-1 1c.6 1.6 1.8 2.8 3.3 3.4l1-1c.7-.5 3.2.5 3.2 1.5 0 1.3-1.4 2.4-2.6 2.2C10.6 16.8 7.8 14 7.3 10 7 8.6 7.9 7 9 7z" fill="#d7e5f5"/></svg>
  <span>Call Us: 800 555 0142</span>
</div>
<span class="abs search-label">Site Search:</span>
<div class="abs search-input">Search</div>
<div class="abs search-btn">
  <svg width="12" height="12" viewBox="0 0 12 12"><circle cx="5" cy="5" r="3.5" fill="none" stroke="#fff" stroke-width="1.8"/><path d="M7.6 7.6L11 11" stroke="#fff" stroke-width="2"/></svg>
</div>

<div class="abs panel"></div>

<div class="abs brand"><span class="brand-mark"></span><span class="brand-name">RIGLINE</span></div>
<span class="abs brand-tag">RENTAL EQUIPMENT AND TOOLS</span>

<nav class="abs nav">
  <a class="active" href="#">Home</a>
  <a href="#">About Us</a>
  <a href="#">Mission &amp; Vision</a>
  <a href="#">Services</a>
  <a href="#">Our Customers</a>
  <a href="#">Contact</a>
</nav>
<div class="abs nav-rule"></div>

<div class="abs hero" role="img" aria-label="Offshore oil platform at sea with a worker in hard hat speaking on a radio"></div>
<h1 class="abs hero-title">RIGLINE</h1>
<p class="abs hero-copy">To promote the healing process by providing smart solutions for our customers and the patients they serve.</p>
<div class="abs hero-btn login">Login <span>▼</span></div>
<div class="abs hero-btn join">Join Us <span>▼</span></div>

<div class="abs dots"><span></span><span></span><span></span><span></span><span class="on"></span></div>

<h2 class="abs h-section" style="left:186px;top:474px">Welcome <em>to Rigline</em></h2>
<div class="abs h-rule" style="left:185px;top:496px;width:179px"></div>
<p class="abs intro">As established in 2014 Rigline Company is one of the fast growing oil/industrial services companies in United Arab Emirates. The company adds value through the entire life cycle of rental equipment as well as manufacture and building facilities. The scope of work includes all types of rental tools and equipment and building and designs all products as per the client requirements, Rigline hence have different activities to cover all rental enquiries for oil services companies as well as industrial companies s rental equipment and tools companies struggle to meet burgeon-ing local demand, the quest for rental equipment and tools leads to deeper scope , harsher environments and complex solutions for maximizing their assets. All of these conditions require</p>
<div class="abs more" style="left:183px;top:579px">read more</div>

<h2 class="abs h-section" style="left:186px;top:630px">Rigline <em>Rental</em></h2>
<h2 class="abs h-section" style="left:379px;top:630px">Rigline <em>Equipment</em></h2>
<h2 class="abs h-section" style="left:573px;top:630px">Transportation <em>Services</em></h2>
<h2 class="abs h-section" style="left:762px;top:630px">Management <em>Services</em></h2>
<div class="abs h-rule" style="left:185px;top:657px;width:180px"></div>
<div class="abs h-rule" style="left:378px;top:657px;width:180px"></div>
<div class="abs h-rule" style="left:570px;top:657px;width:180px"></div>
<div class="abs h-rule" style="left:762px;top:657px;width:180px"></div>

<div class="abs col-img" style="left:185px;background:linear-gradient(160deg,#0d1f12,#2f6b2a 55%,#0b1a10)" role="img" aria-label="Refinery lit at night"></div>
<div class="abs col-img" style="left:378px;background:linear-gradient(180deg,#b9c6d2 0%,#8796a3 55%,#6f747a 100%)" role="img" aria-label="Rows of mud tank units in a yard"></div>
<div class="abs col-img" style="left:570px;background:linear-gradient(180deg,#5aa0e0 0%,#7db6e6 40%,#d8b32a 60%,#8a8a80 100%)" role="img" aria-label="Large yellow mobile crane truck"></div>
<div class="abs col-img" style="left:762px;background:linear-gradient(180deg,#d9dfe4 0%,#c2c8cc 50%,#d8683a 70%,#8b8d8c 100%)" role="img" aria-label="Truck crane lifting an orange site cabin"></div>

<ul class="abs col-list" style="left:185px">
  <li>Rental mud tanks</li><li>Rental mud cutting skips</li><li>Rental offshore/onshore cargo baskets</li><li>Rental chemical baskets</li><li>Rental offshore container workshop</li><li>Rental open top and half height containers</li>
</ul>
<ul class="abs col-list" style="left:377px">
  <li>Rental Mud coolers</li><li>2- Rental screw conveyors</li><li>Rental air compressors Zone I/ Zone II</li><li>Rental diesel generators Zone I/Zone II</li><li>Rental diesel driven centrifugal pumps</li><li>Rental oil field lighting towers</li>
</ul>
<ul class="abs col-list" style="left:573px">
  <li>Rental forklift (all capacity)</li><li>Rental cranes (all capacity)</li><li>Rental loader (multiple purposes)</li><li>Rental tanker trucks (transporting fluids&amp;</li><li>drilling fluids)</li><li>Flatbed trailers</li>
</ul>
<ul class="abs col-list" style="left:767px">
  <li>Tank cleaning services</li><li>Contaminated water treatment services</li><li>Solvent recycling units services</li><li>Waste acid treatment services</li><li>Solvent recycling units services</li><li>Waste acid treatment services</li>
</ul>

<div class="abs more" style="left:183px;top:924px">read more</div>
<div class="abs more" style="left:375px;top:922px">read more</div>
<div class="abs more" style="left:579px;top:922px">read more</div>
<div class="abs more" style="left:774px;top:922px">read more</div>

<div class="abs top-line"></div>
<div class="abs top-btn"><span>^</span><span>TOP</span></div>

<h3 class="abs f-head" style="left:184px">Our Services</h3>
<h3 class="abs f-head" style="left:363px">Clients Testimonials</h3>
<h3 class="abs f-head" style="left:592px">Area Of Fucus</h3>
<h3 class="abs f-head" style="left:793px">Contact Us</h3>

<ul class="abs f-list" style="left:184px;top:999px;width:129px">
  <li>Facility &amp; Recourses</li><li>Company organization</li><li>Health, Safety and Environment</li><li>Services Quality</li><li>Rigline Approach</li><li>Sustaibable Development</li>
</ul>
<p class="abs quote">" Lorem ipsum dolor sit amet, consectetur adipisicing elit, sed do eiusmod tempor incidid-unt labore dolore magna aliqua. Ut enim ad minim veniam, quis nostrud exercitation ullamco laboris nisi ut aliquip ex ea commodo consequat."</p>
<div class="abs quote-rule"></div>
<p class="abs quote-by"><b>Dana Moreau</b>, Operations Lead, Gulfline Drilling</p>
<ul class="abs f-list" style="left:592px;top:999px;width:130px">
  <li>Rental and Manufacture</li><li>Mud tanks &amp; Cutting Skips</li><li>Heavy Trucks &amp; Lifting Equipment</li><li>Rental Equipment</li><li>Industrial and oil field services</li><li>Sspecialized transportation and trucking</li>
</ul>
<p class="abs contact">PO Box No 40718<br>loreum ipsum<br>oloreum ispdum<br><br>Telephone/Fax: 800 555 0199<br><br>General: desk@rigline-rentals.com<br>Support:&nbsp; desk@rigline-rentals.com</p>

<div class="abs foot-rule"></div>
<p class="abs copyright">© 2014Copyright <b>Rigline</b>. All Rights Reserved</p>
<p class="abs subscribe">Subscribe to<br>our newsletter</p>
<div class="abs sub-input">yourname@email.com</div>
<div class="abs sub-btn">Submit</div>

</body>
</html>
```